Dalwin Electric Supply, Inc. Business Card Design

We are an Electrical Distributor looking for a Modern, Professional Business Card design.

Target Market(s)

Residential Commercial Industrial

Industry/Entity Type

Electrical

Contact Information for Business Card

Dalwin Electric Supply, Inc.
418 Tallow Creek Road
Brennick, NC 27514
555-312-4867
555-312-4921 Fax
dalwinelectric@voltmail.example

```html
<!DOCTYPE html>
<html lang="en">
<head>
<meta charset="utf-8">
<title>Dalwin Electric Supply, Inc. — Business Card</title>
<link rel="stylesheet" href="https://fonts.googleapis.com/css2?family=Oswald:wght@300;400;600&display=swap">
<style>
  :root {
    --backdrop: #d9d9d9;
    --card-dark: #231f20;
    --card-green: #0b5e37;
    --accent-lime: #c6d98a;
    --text-white: #ffffff;
    --icon-green: #0b5e37;
  }
  * { box-sizing: border-box; margin: 0; padding: 0; }
  html, body {
    width: 1200px; height: 800px; overflow: hidden;
    background: var(--backdrop);
  }
  body {
    display: flex; align-items: center; justify-content: center;
    font-family: "Oswald", "Arial Narrow", sans-serif;
  }
  .business-card {
    width: 1050px; height: 600px;
    border-radius: 34px; overflow: hidden;
    display: flex; flex-direction: column;
  }
  .brand-band {
    flex: 0 0 290px;
    background: var(--card-dark);
    display: flex; align-items: center; justify-content: center;
    gap: 26px;
  }
  .brand-dot {
    width: 70px; height: 70px; border-radius: 50%;
    background: var(--accent-lime);
  }
  .brand-name {
    color: var(--accent-lime);
    font-weight: 600;
    font-size: 78px;
    letter-spacing: 1px;
    text-transform: uppercase;
    line-height: 1;
  }
  .contact-band {
    flex: 1;
    background: var(--card-green);
    color: var(--text-white);
    display: flex; align-items: center; justify-content: center;
    padding-bottom: 10px;
  }
  .address-block {
    text-align: right;
    font-weight: 400;
    font-size: 38px;
    line-height: 1.22;
    padding-right: 30px;
  }
  .contact-divider {
    width: 2px; align-self: stretch;
    margin: 40px 0 36px;
    background: var(--text-white);
  }
  .contact-list {
    list-style: none;
    padding-left: 30px;
    font-size: 38px;
    font-weight: 400;
    line-height: 1;
  }
  .contact-item {
    display: flex; align-items: center; gap: 18px;
    margin: 14px 0;
  }
  .contact-icon {
    width: 48px; height: 48px; border-radius: 50%;
    background: var(--text-white);
    display: flex; align-items: center; justify-content: center;
    flex: 0 0 48px;
  }
  .contact-icon svg { width: 28px; height: 28px; fill: var(--icon-green); }
</style>
</head>
<body>
  <article class="business-card">
    <header class="brand-band">
      <span class="brand-dot" aria-hidden="true"></span>
      <h1 class="brand-name">Dalwin Electric Supply</h1>
    </header>
    <section class="contact-band">
      <address class="address-block">
        Dalwin Electric Supply, Inc.<br>
        418 Tallow Creek Road<br>
        Brennick, NC 27514
      </address>
      <div class="contact-divider" aria-hidden="true"></div>
      <ul class="contact-list">
        <li class="contact-item">
          <span class="contact-icon" aria-label="Phone">
            <svg viewBox="0 0 24 24"><path d="M6.6 10.8a15.1 15.1 0 0 0 6.6 6.6l2.2-2.2a1 1 0 0 1 1-.25 11.4 11.4 0 0 0 3.6.57 1 1 0 0 1 1 1V20a1 1 0 0 1-1 1A17 17 0 0 1 3 4a1 1 0 0 1 1-1h3.5a1 1 0 0 1 1 1c0 1.25.2 2.45.57 3.6a1 1 0 0 1-.25 1z"/></svg>
          </span>
          555-312-4867
        </li>
        <li class="contact-item">
          <span class="contact-icon" aria-label="Fax">
            <svg viewBox="0 0 24 24"><path d="M7 2h8l3 3v5H7z M9 5v1h6V5z M5 11h14a2 2 0 0 1 2 2v7a2 2 0 0 1-2 2H5a2 2 0 0 1-2-2v-7a2 2 0 0 1 2-2z M7 14v2h2v-2z m4 0v2h2v-2z m4 0v2h2v-2z M7 18v2h2v-2z m4 0v2h2v-2z m4 0v2h2v-2z"/></svg>
          </span>
          555-312-4921
        </li>
        <li class="contact-item">
          <span class="contact-icon" aria-label="Email">
            <svg viewBox="0 0 24 24"><path d="M3 5h18a1 1 0 0 1 1 1v12a1 1 0 0 1-1 1H3a1 1 0 0 1-1-1V6a1 1 0 0 1 1-1zm1 2.2V17h16V7.2l-8 5.6zM5.2 7 12 11.7 18.8 7z"/></svg>
          </span>
          dalwinelectric@voltmail.example
        </li>
      </ul>
    </section>
  </article>
</body>
</html>
```